Velorin Banner Design

We need banners for new company Velorin Holdings Limited located in Hong Kong. Velorin is an global online business platform, needs clean white, blue and red color mix banners.

Reason: I am extending for final design

Target Market(s)

Velorin an online Business Company have a target home based business owners and DIY website seekers.

Industry/Entity Type

Business

Colors
0355a3
ec2027
ffffff

Requirements
Must have
• Free Sign Up Button and Velorin Logo

```html
<!DOCTYPE html>
<html lang="en">
<head>
<meta charset="utf-8">
<title>Velorin Banner Set</title>
<link rel="stylesheet" href="https://fonts.googleapis.com/css2?family=Roboto+Condensed:wght@400;700&display=swap">
<style>
  :root {
    --blue: #0355a3;
    --red: #ec2027;
    --white: #ffffff;
    --grey: #9b9b9b;
    --label: #4a4a4a;
    --frame: #cfcfcf;
    --btn-top: #ffffff;
    --btn-bottom: #9fd0f2;
    --btn-edge: #3c8ed4;
  }
  * { box-sizing: border-box; margin: 0; padding: 0; }
  html, body { width: 784px; height: 1200px; overflow: hidden; background: var(--white); }
  body { font-family: "Roboto Condensed", "Arial Narrow", sans-serif; }

  .stage { position: absolute; left: 0; top: 0; width: 490px; height: 750px; transform: scale(1.6); transform-origin: 0 0; }

  .banner { position: absolute; background: var(--white); border: 1px solid var(--frame); overflow: hidden; }
  .banner .panel { position: absolute; left: 0; top: 0; bottom: 0; background: var(--blue); }
  .banner .wave { position: absolute; left: 0; top: 0; width: 100%; height: 100%; }
  .headline { position: absolute; color: var(--white); line-height: 1.18; z-index: 1; }
  .tagline { position: absolute; color: var(--white); line-height: 1.2; z-index: 1; white-space: nowrap; }
  .logo-vertical {
    position: absolute; color: var(--grey); font-weight: 700; letter-spacing: 0.06em;
    writing-mode: vertical-rl; transform: rotate(180deg); white-space: nowrap; z-index: 2;
  }
  .btn-signup {
    position: absolute; display: flex; align-items: center; justify-content: center;
    border-radius: 999px; border: 1px solid var(--btn-edge);
    background: linear-gradient(var(--btn-top) 0%, #e4f2fc 45%, var(--btn-bottom) 100%);
    color: var(--red); font-weight: 700; white-space: nowrap; z-index: 3;
    box-shadow: 0 1px 2px rgba(0,0,0,.35);
  }
  .size-label { position: absolute; color: var(--label); font-family: Arial, Helvetica, sans-serif; font-size: 16px; }

  /* 468x60 leaderboard */
  .leaderboard { left: 10px; top: 10px; width: 468px; height: 60px; }
  .leaderboard .panel { height: 38px; bottom: auto; right: 0; }
  .leaderboard .headline { left: 6px; top: 2px; font-size: 14px; font-weight: 700; }
  .leaderboard .tagline { left: 8px; top: 44px; font-size: 12.5px; color: var(--red); }
  .leaderboard .btn-signup { left: 354px; top: 6px; width: 110px; height: 22px; font-size: 13px; }
  .leaderboard .logo-inline { position: absolute; right: 6px; bottom: 1px; color: var(--grey); font-weight: 700; font-size: 17px; letter-spacing: 0.06em; z-index: 2; }

  /* 250x250 square */
  .square { left: 22px; top: 128px; width: 250px; height: 250px; }
  .square .panel { width: 207px; }
  .square .headline { left: 13px; top: 6px; font-size: 21px; font-weight: 700; }
  .square .tagline { left: 13px; top: 148px; font-size: 18px; }
  .square .btn-signup { left: 36px; top: 204px; width: 148px; height: 36px; font-size: 20px; }
  .square .logo-vertical { left: 210px; bottom: 8px; font-size: 38px; }

  /* 160x600 skyscraper */
  .skyscraper { left: 312px; top: 118px; width: 160px; height: 602px; }
  .skyscraper .panel { width: 126px; }
  .skyscraper .headline { left: 9px; top: 20px; font-size: 22px; line-height: 1.32; }
  .skyscraper .tagline { left: 9px; top: 365px; font-size: 19px; }
  .skyscraper .btn-signup { left: 6px; top: 543px; width: 148px; height: 40px; font-size: 18px; }
  .skyscraper .logo-vertical { left: 126px; top: 20px; font-size: 34px; }

  /* 125x125 button */
  .button-square { left: 22px; top: 432px; width: 125px; height: 125px; }
  .button-square .panel { width: 103px; }
  .button-square .headline { left: 6px; top: 3px; font-size: 10px; font-weight: 700; }
  .button-square .tagline { left: 8px; top: 75px; font-size: 9px; }
  .button-square .btn-signup { left: 14px; top: 101px; width: 78px; height: 16px; font-size: 9px; }
  .button-square .logo-vertical { left: 104px; bottom: 4px; font-size: 18px; }

  /* 120x160 */
  .vertical-small { left: 172px; top: 470px; width: 120px; height: 160px; }
  .vertical-small .panel { width: 100px; }
  .vertical-small .headline { left: 5px; top: 8px; width: 93px; font-size: 9px; letter-spacing: -0.1px; }
  .vertical-small .tagline { left: 5px; top: 104px; font-size: 9px; }
  .vertical-small .btn-signup { left: 12px; top: 132px; width: 76px; height: 16px; font-size: 9px; }
  .vertical-small .logo-vertical { left: 101px; bottom: 6px; font-size: 17px; }

  /* 120x90 */
  .compact { left: 22px; top: 602px; width: 120px; height: 90px; }
  .compact .panel { width: 100px; }
  .compact .headline { left: 5px; top: 4px; font-size: 9.5px; font-weight: 700; }
  .compact .btn-signup { left: 12px; top: 76px; width: 72px; height: 12px; font-size: 8px; }
  .compact .logo-vertical { left: 101px; bottom: 4px; font-size: 14px; }
</style>
</head>
<body>
<div class="stage">

  <section class="banner leaderboard">
    <div class="panel"></div>
    <svg class="wave" viewBox="0 0 468 60" preserveAspectRatio="none" aria-hidden="true">
      <path d="M0 38 L250 38 C320 36 380 20 468 0 L468 18 C400 30 330 42 260 43 L0 43 Z" fill="var(--red)"/>
    </svg>
    <p class="headline">Create your Own eCommerce Website at Mininum<br>$10/month and Start Earning at the same time.</p>
    <p class="tagline">Revolutionary Single Line Affiliate Programs</p>
    <span class="btn-signup">FREE SIGN UP</span>
    <span class="logo-inline">VELORIN</span>
  </section>
  <span class="size-label" style="left:210px; top:88px;">468x60</span>

  <section class="banner square">
    <div class="panel"></div>
    <svg class="wave" viewBox="0 0 250 250" preserveAspectRatio="none" aria-hidden="true">
      <path d="M0 140 C70 128 160 120 232 142 C220 190 212 225 196 250 L0 250 Z" fill="var(--red)"/>
    </svg>
    <p class="headline">Create your Own<br>eCommerce Website<br>at Mininum $10/mo.<br>and Start Earning<br>at the same time.</p>
    <p class="tagline">Revolutionary Single<br>Line Affiliate Programs</p>
    <span class="btn-signup">FREE SIGN UP</span>
    <span class="logo-vertical">VELORIN</span>
  </section>
  <span class="size-label" style="left:108px; top:388px;">250x250</span>

  <section class="banner skyscraper">
    <div class="panel"></div>
    <svg class="wave" viewBox="0 0 160 602" preserveAspectRatio="none" aria-hidden="true">
      <path d="M0 355 C70 350 130 335 156 300 C158 360 150 450 128 520 C110 560 90 590 72 602 L48 602 C70 560 72 510 60 490 L0 478 Z" fill="var(--red)"/>
    </svg>
    <p class="headline">Create your<br>Own<br>eCommerce<br>Website at<br>Mininum<br>$10/month<br>and Start<br>Earning<br>at the<br>same time.</p>
    <p class="tagline">Revolutionary<br>Single Line<br>Affiliate Programs</p>
    <span class="btn-signup">FREE SIGN UP</span>
    <span class="logo-vertical">VELORIN</span>
  </section>
  <span class="size-label" style="left:228px; top:700px;">160x600</span>

  <section class="banner button-square">
    <div class="panel"></div>
    <svg class="wave" viewBox="0 0 125 125" preserveAspectRatio="none" aria-hidden="true">
      <path d="M0 72 C35 66 80 62 116 72 C112 98 108 112 100 125 L0 125 Z" fill="var(--red)"/>
    </svg>
    <p class="headline">Create your Own<br>eCommerce Website<br>at Mininum $10/mo.<br>and Start Earning<br>at the same time.</p>
    <p class="tagline">Revolutionary Single<br>Line Affiliate Programs</p>
    <span class="btn-signup">FREE SIGN UP</span>
    <span class="logo-vertical">VELORIN</span>
  </section>
  <span class="size-label" style="left:46px; top:566px;">125x125</span>

  <section class="banner vertical-small">
    <div class="panel"></div>
    <svg class="wave" viewBox="0 0 120 160" preserveAspectRatio="none" aria-hidden="true">
      <path d="M0 98 C35 92 80 86 112 98 C108 128 104 146 96 160 L0 160 Z" fill="var(--red)"/>
    </svg>
    <p class="headline">Create your Own eCommerce Website at Mininum $10/mo. and Start Earning at the same time.</p>
    <p class="tagline">Revolutionary Single<br>Line Affiliate Programs</p>
    <span class="btn-signup">FREE SIGN UP</span>
    <span class="logo-vertical">VELORIN</span>
  </section>
  <span class="size-label" style="left:194px; top:642px;">120x160</span>

  <section class="banner compact">
    <div class="panel"></div>
    <svg class="wave" viewBox="0 0 120 90" preserveAspectRatio="none" aria-hidden="true">
      <path d="M0 68 C35 64 80 60 112 68 C110 78 106 85 102 90 L0 90 Z" fill="var(--red)"/>
    </svg>
    <p class="headline">Create your Own<br>eCommerce<br>Website at Mininum<br>$10/mo. and Start<br>Earning at the<br>same time.</p>
    <span class="btn-signup">FREE SIGN UP</span>
    <span class="logo-vertical">VELORIN</span>
  </section>
  <span class="size-label" style="left:50px; top:702px;">120x90</span>

</div>
</body>
</html>
```